Postcard Design

We are a full service lawn maintenace and landscapig company. Everything from maintenance, fertilizer programs, to design and install.
I would like the card to have a classy look including our logo which is attached. The logo would just have to contain the lettering and the swooshes not the pine tree background if not needed.

Industry/Entity Type

It Company

```html
<!DOCTYPE html>
<html lang="en">
<head>
<meta charset="utf-8">
<title>Tall Cedar Landscaping Postcard</title>
<link href="https://fonts.googleapis.com/css2?family=Archivo+Black&family=Cinzel:wght@700&family=EB+Garamond&family=Raleway:wght@200&display=swap" rel="stylesheet">
<style>
  :root {
    --forest: #0f4d16;
    --sage: #86aa86;
    --sage-light: #b8cdb5;
    --leaf-text: #2f5b30;
    --sun-yellow: #f6e31a;
    --accent-orange: #f0652a;
    --white: #ffffff;
    --tulip-red: #d8321c;
    --tulip-orange: #ee7a22;
    --tulip-yellow: #f2c62a;
    --lawn: #4f7a2a;
    --phone-green: #7fcf3a;
  }
  html, body { margin: 0; padding: 0; overflow: hidden; background: var(--white); }
  .postcard {
    position: relative;
    width: 1200px;
    height: 863px;
    overflow: hidden;
    background: var(--white);
  }
  .backdrop { position: absolute; inset: 0; }
  .accent-stripe {
    position: absolute; left: 0; top: 0; width: 20px; height: 100%;
    background: linear-gradient(90deg, #f36d2c, var(--accent-orange));
  }
  .brand {
    position: absolute; left: 60px; top: 86px; width: 470px; text-align: center;
    font-family: "Cinzel", serif; font-weight: 700; color: var(--forest);
  }
  .brand-name { margin: 0; font-size: 48px; line-height: 46px; letter-spacing: 1px; }
  .brand-address {
    margin: 12px 0 0; font-size: 11px; line-height: 13px; color: var(--forest);
    letter-spacing: 0.5px;
  }
  .cta {
    position: absolute; left: 150px; top: 273px; width: 295px; margin: 0; text-align: center;
    font-family: "Cinzel", serif; font-weight: 700; font-size: 21px; line-height: 39px;
    color: var(--white); letter-spacing: 1.5px;
    text-shadow: 0 0 3px rgba(60, 100, 60, 0.35);
  }
  .tagline {
    position: absolute; left: 500px; top: 214px; width: 590px; margin: 0; text-align: center;
    font-family: "Raleway", sans-serif; font-weight: 200; font-size: 33px; line-height: 45px;
    color: var(--white);
  }
  .services {
    position: absolute; top: 430px; left: 85px; display: flex;
    font-family: "EB Garamond", serif; font-size: 17.5px; line-height: 22.5px; color: var(--leaf-text);
  }
  .services ul { list-style: none; margin: 0; padding: 0; text-align: center; }
  .services .col-1 { width: 140px; }
  .services .col-2 { width: 160px; color: #7e9b7c; }
  .services .col-3 { width: 140px; color: #5f7e5e; }
  .phone-art {
    position: absolute; left: 500px; top: 728px; width: 112px; height: 122px;
    border-radius: 14px;
    background: radial-gradient(circle at 50% 55%, #9ee05a 0%, var(--phone-green) 45%, rgba(127, 207, 58, 0) 75%);
  }
  .phone-number {
    position: absolute; left: 634px; top: 770px; margin: 0;
    font-family: "Archivo Black", sans-serif; font-size: 65px; line-height: 80px; letter-spacing: 1px;
    color: var(--sun-yellow);
    -webkit-text-stroke: 1.5px #7a6a00;
    text-shadow: 2px 3px 3px rgba(0,0,0,0.35);
  }
</style>
</head>
<body>
<main class="postcard">
  <svg class="backdrop" width="1200" height="863" viewBox="0 0 1200 863">
    <defs>
      <linearGradient id="tulipTones" x1="0" y1="0" x2="1" y2="0.3">
        <stop offset="0" stop-color="var(--tulip-red)"/>
        <stop offset="0.45" stop-color="var(--tulip-orange)"/>
        <stop offset="0.8" stop-color="var(--tulip-yellow)"/>
        <stop offset="1" stop-color="#e9c93c"/>
      </linearGradient>
      <linearGradient id="gardenTop" x1="0" y1="0" x2="0" y2="1">
        <stop offset="0" stop-color="var(--lawn)"/>
        <stop offset="0.3" stop-color="var(--lawn)" stop-opacity="0"/>
      </linearGradient>
      <linearGradient id="groundFade" x1="0" y1="0" x2="0" y2="1">
        <stop offset="0.55" stop-color="#fff" stop-opacity="0"/>
        <stop offset="1" stop-color="#fff" stop-opacity="1"/>
      </linearGradient>
      <linearGradient id="leftFade" x1="0" y1="0" x2="1" y2="0">
        <stop offset="0" stop-color="#fff" stop-opacity="0.85"/>
        <stop offset="0.2" stop-color="#fff" stop-opacity="0"/>
      </linearGradient>
      <linearGradient id="sageFade" x1="0" y1="0" x2="1" y2="0">
        <stop offset="0.05" stop-color="#fff"/>
        <stop offset="0.38" stop-color="var(--sage-light)"/>
        <stop offset="0.6" stop-color="var(--sage)"/>
        <stop offset="1" stop-color="var(--sage)"/>
      </linearGradient>
      <linearGradient id="sageVertical" x1="0" y1="0" x2="0" y2="1">
        <stop offset="0.55" stop-color="#fff" stop-opacity="0"/>
        <stop offset="1" stop-color="#fff" stop-opacity="0.95"/>
      </linearGradient>
      <radialGradient id="sunTones">
        <stop offset="0.3" stop-color="var(--accent-orange)"/>
        <stop offset="0.55" stop-color="var(--sun-yellow)"/>
        <stop offset="1" stop-color="var(--sun-yellow)" stop-opacity="0"/>
      </radialGradient>
    </defs>

    <path class="header-band" d="M380 0 H1200 V430 H900 Z" fill="var(--forest)"/>

    <g role="img" aria-label="Photo of a garden bed full of red, orange and yellow tulips">
      <rect x="20" y="400" width="1180" height="463" fill="url(#tulipTones)"/>
      <rect x="20" y="400" width="1180" height="463" fill="url(#gardenTop)"/>
      <rect x="20" y="400" width="1180" height="463" fill="url(#leftFade)"/>
      <rect x="20" y="400" width="1180" height="463" fill="url(#groundFade)"/>
    </g>

    <path class="white-sweep" d="M20 0 H640 C980 10 1215 130 1200 300 C1185 440 900 560 500 600 C300 618 120 612 20 605 Z" fill="#fff"/>
    <path class="gold-rim" d="M560 10 C930 18 1190 130 1185 290 C1178 430 880 545 460 585 C300 598 140 595 20 588" fill="none" stroke="var(--sun-yellow)" stroke-width="3"/>
    <path class="sage-oval" d="M20 0 H560 C930 18 1184 130 1183 290 C1176 428 880 543 460 583 C300 596 140 593 20 586 Z" fill="url(#sageFade)"/>
    <path d="M20 0 H560 C930 18 1184 130 1183 290 C1176 428 880 543 460 583 C300 596 140 593 20 586 Z" fill="url(#sageVertical)"/>

    <rect x="1060" y="22" width="116" height="112" fill="url(#sunTones)" role="img" aria-label="Small sun illustration with orange swirl"/>
  </svg>

  <div class="accent-stripe"></div>

  <header class="brand">
    <h1 class="brand-name">TALL CEDAR<br>LANDSCAPING</h1>
    <p class="brand-address">18210 Maple Row<br>Fairview, MI 48000<br>555-014-2270</p>
  </header>

  <p class="cta">Call Us<br>for a free<br>consultation!</p>

  <p class="tagline">A full service lawn maintenace and<br>landscaping company.<br>Everything from maintenance, fertilizer<br>programs, to design and install.</p>

  <section class="services" aria-label="Services">
    <ul class="col-1"><li>Mowing</li><li>Plugging</li><li>Trimming</li><li>Leaf Blowing</li><li>Pruning</li><li>Tilling</li></ul>
    <ul class="col-2"><li>Weeding</li><li>Mulching</li><li>Planting</li><li>Sodding</li><li>Fertilizing</li><li>Seeding</li></ul>
    <ul class="col-3"><li>Tree Removal</li><li>Debris Removal</li><li>Retaining Walls</li><li>Weed Control</li><li>Gutter Cleaning</li><li>Pine Needles</li></ul>
  </section>

  <div class="phone-art" role="img" aria-label="Illustration of a green rotary telephone"></div>
  <p class="phone-number">xxx-555-0193</p>
</main>
</body>
</html>
```